Horticulture Consulting Company Premium Card

We are looking for new design for a premium business card.
Our cards will be printed on glossy and embossed premium card stock.

Target Market(s)

Horticulture business owners needing our consulting services

Contact Information for Business Card

Marcus Thorne
(555) 348-2916
Marcus@velturaq.com

Requirements
Must have
• Company Logo and Contact information.
• Some additional work to add interest to the card
Should not have
• Red or Yellow

```html
<!DOCTYPE html>
<html lang="en">
<head>
<meta charset="utf-8">
<title>Veltura Grow Co. — Business Card</title>
<link rel="stylesheet" href="https://fonts.googleapis.com/css2?family=Fjalla+One&family=Ubuntu:wght@400;500&display=swap">
<style>
  :root {
    --bg: #e4e6e8;
    --card: #ffffff;
    --brand-blue: #0b6fb8;
    --brand-green: #3bab45;
    --ink-dark: #2d3a40;
    --ink-light: #ffffff;
  }
  * { margin: 0; padding: 0; box-sizing: border-box; }
  html, body {
    width: 1200px; height: 1200px; overflow: hidden;
    background: var(--bg);
  }
  .card {
    position: absolute;
    left: 100px; top: 314px;
    width: 1000px; height: 572px;
    background: var(--card);
    box-shadow: 0 10px 30px rgba(0,0,0,0.12);
    overflow: hidden;
  }
  .accent-bar {
    position: absolute;
    left: 0; top: 245px;
    width: 58px; height: 240px;
    background: var(--brand-green);
  }
  .brand {
    position: absolute;
    left: 150px; top: 280px;
    width: 330px;
    text-align: center;
  }
  .brand-mark {
    display: flex; align-items: center; justify-content: center; gap: 14px;
  }
  .brand-dot {
    width: 34px; height: 34px; border-radius: 50%;
    background: var(--brand-green);
  }
  .brand-name {
    font-family: "Fjalla One", sans-serif;
    font-size: 52px; line-height: 1;
    color: var(--brand-blue);
    letter-spacing: 1px;
  }
  .brand-tagline {
    margin-top: 14px;
    font-family: "Ubuntu", sans-serif;
    font-weight: 500;
    font-size: 14px;
    letter-spacing: 1.2px;
    text-transform: uppercase;
    color: var(--ink-dark);
    border-top: 2px solid var(--brand-green);
    border-bottom: 2px solid var(--brand-green);
    padding: 5px 0;
  }
  .contact-panel {
    position: absolute;
    left: 520px; top: 120px;
    width: 480px; height: 222px;
    background: var(--brand-blue);
  }
  .contact-notch {
    position: absolute;
    right: 0; top: 128px;
    width: 150px; height: 94px;
    background: var(--card);
  }
  .contact-body {
    position: absolute;
    left: 60px; top: 40px;
  }
  .person-name {
    font-family: "Fjalla One", sans-serif;
    font-size: 48px; line-height: 1;
    color: var(--brand-green);
    text-transform: uppercase;
    letter-spacing: 0.5px;
  }
  .person-role {
    font-family: "Ubuntu", sans-serif;
    font-size: 22px;
    color: var(--ink-light);
    margin-top: 4px;
  }
  .contact-list {
    list-style: none;
    margin-top: 20px;
    font-family: "Ubuntu", sans-serif;
    font-size: 23px;
    color: var(--ink-light);
  }
  .contact-list li {
    display: flex; align-items: center; gap: 12px;
    margin-bottom: 6px;
  }
  .contact-list svg { width: 18px; height: 18px; flex: none; }
</style>
</head>
<body>
  <div class="card">
    <div class="accent-bar"></div>

    <div class="brand">
      <div class="brand-mark">
        <span class="brand-dot"></span>
        <span class="brand-name">VELTURA GROW</span>
      </div>
      <div class="brand-tagline">Controlled Environment Agriculture</div>
    </div>

    <div class="contact-panel">
      <div class="contact-notch"></div>
      <div class="contact-body">
        <div class="person-name">Marcus Thorne</div>
        <div class="person-role">manager</div>
        <ul class="contact-list">
          <li>
            <svg viewBox="0 0 24 24" aria-hidden="true"><path fill="#3bab45" d="M6.6 10.8a15.1 15.1 0 0 0 6.6 6.6l2.2-2.2c.3-.3.7-.4 1-.2 1.1.4 2.3.6 3.6.6.6 0 1 .4 1 1V20c0 .6-.4 1-1 1A17 17 0 0 1 3 4c0-.6.4-1 1-1h3.5c.6 0 1 .4 1 1 0 1.3.2 2.5.6 3.6.1.3 0 .7-.2 1z"/></svg>
            <span>(555) 348-2916</span>
          </li>
          <li>
            <svg viewBox="0 0 24 24" aria-hidden="true"><path fill="#3bab45" d="M2 5h20v14H2z"/><path fill="none" stroke="#0b6fb8" stroke-width="1.8" d="M2.5 5.5 12 13l9.5-7.5"/></svg>
            <span>Marcus@velturaq.com</span>
          </li>
        </ul>
      </div>
    </div>
  </div>
</body>
</html>
```